Monument sign* - Law Firm

*I am installing a monument sign that has LED, as well as backlit elements. I am seeking help in designing the backlit portion of the sign. The Backlit sign will be 12’ x 4’.

We are looking for a classic, yet eye-catching sign to help new and current clients find our firm as well as bring in future clients. One of our goals is that people who drive by on a regular basis remember our sign (and us) for any future legal need.

Target Market(s)

Current and future clientele

Industry/Entity Type

Law Firm

Font styles to use
Serif
Sans Serif

Colors
b1b1b1
333333

Requirements
Must have
• Business name: Hargrove Law Firm, Inc.
• Website: www.hargrovelawfirm-example.com
• Telephone: (555)214-3679
• Our firm's logo
Nice to have
• Color preference is black, taupe, and white. A photo for reference of the office coloring is uploaded.
• We currently have an established logo which our firm has been using for more than 10 years. Our logo has been used in advertising, commercials, letterhead, and on-site. We are looking to transition from brown/rust/cream to the black/taupe/white color scheme.
Should not have
• Cheesy slogans; character designs; directions; additional symbols outside of the firm's logo.

```html
<!DOCTYPE html>
<html lang="en">
<head>
<meta charset="utf-8">
<title>Hargrove Law Firm, Inc. – Monument Sign</title>
<link rel="stylesheet" href="https://fonts.googleapis.com/css2?family=Cinzel:wght@400;600;700&display=swap">
<style>
  :root {
    --black: #000000;
    --taupe: #8e8276;
    --white: #ffffff;
  }
  html, body {
    margin: 0;
    padding: 0;
    width: 1200px;
    height: 401px;
    overflow: hidden;
    background: var(--white);
  }
  .sign {
    display: block;
    width: 1200px;
    height: 401px;
  }
  .sign-field { fill: var(--black); }
  .sign-corner { fill: var(--white); }
  .header-band {
    fill: var(--taupe);
    stroke: var(--white);
    stroke-width: 3;
  }
  .sign-text {
    font-family: "Cinzel", "Times New Roman", serif;
    fill: var(--white);
  }
  .website { font-weight: 700; font-size: 25px; letter-spacing: 1px; }
  .phone { font-weight: 400; font-size: 21px; }
  .firm-name { font-weight: 700; font-size: 100px; }
  .logo-name { font-weight: 600; font-size: 34px; }
</style>
</head>
<body>
<svg class="sign" viewBox="0 0 1200 401" xmlns="http://www.w3.org/2000/svg" role="img" aria-label="Hargrove Law Firm, Inc. sign">
  <rect class="sign-field" x="0" y="0" width="1200" height="401"/>
  <path class="sign-corner" d="M0 0 H150 V52 Q150 70 132 70 H0 Z"/>

  <path class="header-band" d="M150 -2 H1202 V66 H392 Q374 66 374 84 V232 Q374 250 356 250 H168 Q150 250 150 232 Z"/>

  <text class="sign-text website" x="1180" y="50" text-anchor="end">www.hargrovelawfirm-example.com</text>
  <text class="sign-text phone" x="1168" y="113" text-anchor="end">Tel : (555)214-3679</text>

  <text class="sign-text logo-name" x="262" y="170" text-anchor="middle">Hargrove</text>

  <text class="sign-text firm-name" x="72" y="377" textLength="1076" lengthAdjust="spacingAndGlyphs">Hargrove Law Firm, Inc.</text>
</svg>
</body>
</html>
```